Business Card Design Project

Refresh of logo attached. Require text underneath to be more ledgible, crisper & cleaner.

Overall, staying with same colour scheme need a brighter, crisper, easily readible business card style.

Industry/Entity Type

Business

```html
<!DOCTYPE html>
<html lang="en">
<head>
<meta charset="utf-8">
<title>NORVA Business Card Set</title>
<link rel="stylesheet" href="https://fonts.googleapis.com/css2?family=EB+Garamond:wght@500&family=Source+Sans+3:wght@400;600&display=swap">
<style>
  :root {
    --stage: #3b2b21;
    --paper: #ffffff;
    --ink: #3d3d3d;
    --teal: #2a8bb0;
    --teal-deep: #235a6a;
    --teal-bright: #23829f;
    --charcoal: #3b3b3b;
    --slate: #2a5563;
    --slate-dark: #214a57;
    --faint-grey: #dcdcdc;
    --faint-blue: #dfe6ec;
    --label: #ffffff;
  }
  * { margin: 0; padding: 0; box-sizing: border-box; }
  html, body { width: 1200px; height: 913px; overflow: hidden; }
  body {
    position: relative;
    background: var(--stage);
    font-family: "Source Sans 3", Arial, sans-serif;
  }
  .card {
    position: absolute;
    width: 457px;
    height: 261px;
    box-shadow: 0 3px 8px rgba(0,0,0,.45);
    overflow: hidden;
  }
  .card--front { left: 96px; top: 140px; background: var(--paper); }
  .card--back-light { left: 595px; top: 137px; background: var(--paper); }
  .card--back-charcoal { left: 105px; top: 434px; background: var(--charcoal); }
  .card--back-slate { left: 600px; top: 432px; background: var(--slate); }

  .side-label {
    position: absolute;
    color: var(--label);
    font-size: 34px;
    font-weight: 400;
    line-height: 1;
  }
  .side-label--one { left: 932px; top: 90px; }
  .side-label--two { left: 126px; top: 728px; }
  .side-label--three { left: 955px; top: 715px; }

  .wordmark {
    position: absolute;
    display: flex;
    align-items: center;
    font-family: "EB Garamond", Georgia, serif;
    font-weight: 500;
    line-height: 1;
    white-space: nowrap;
  }
  .wordmark--centered { left: 0; right: 0; justify-content: center; }
  .wordmark__square { display: block; flex: none; }

  /* Front */
  .front-brand { left: 35px; top: 24px; gap: 9px; font-size: 42px; color: var(--ink); }
  .front-brand .wordmark__square { width: 36px; height: 36px; background: var(--teal-deep); }
  .front-rule {
    position: absolute; left: 32px; top: 69px;
    width: 196px; height: 2px; background: var(--ink);
  }
  .front-tagline {
    position: absolute; left: 32px; top: 74px;
    font-size: 6.4px; letter-spacing: .3px; color: var(--ink); white-space: nowrap;
  }
  .front-tagline span { color: var(--teal); }
  .contact-mark {
    position: absolute; left: 37px; top: 196px;
    width: 42px; height: 42px; background: var(--teal-deep);
  }
  .contact-list {
    position: absolute; left: 91px; top: 192px;
    list-style: none; font-size: 11.5px; line-height: 16px; color: var(--teal);
  }
  .contact-list b { display: inline-block; width: 20px; font-weight: 400; }
  .holder { position: absolute; right: 38px; top: 204px; }
  .holder__name {
    font-family: "EB Garamond", Georgia, serif; font-weight: 500;
    font-size: 18px; color: var(--teal-deep); white-space: nowrap;
  }
  .holder__title {
    font-size: 8px; letter-spacing: .5px; color: var(--teal); margin-top: 1px; white-space: nowrap;
  }

  .web {
    position: absolute; font-size: 10.5px; letter-spacing: 3.4px; white-space: nowrap;
  }
  .web--centered { left: 0; right: 0; text-align: center; }

  /* Back 1 */
  .faint-brand { top: 92px; gap: 12px; font-size: 58px; color: var(--faint-grey); }
  .faint-brand .wordmark__square { width: 52px; height: 52px; background: var(--faint-blue); }
  .card--back-light .web { top: 156px; color: var(--teal); }

  /* Back 2 */
  .charcoal-brand { top: 84px; gap: 14px; font-size: 56px; color: var(--teal-bright); }
  .charcoal-brand .wordmark__square { width: 50px; height: 50px; background: var(--teal-deep); }
  .card--back-charcoal .web { top: 224px; letter-spacing: 7px; color: #5c5c5c; }

  /* Back 3 */
  .slate-brand { left: 170px; top: 82px; gap: 14px; font-size: 56px; color: var(--teal-bright); }
  .slate-brand .wordmark__square { width: 50px; height: 50px; background: var(--slate-dark); }
  .card--back-slate .web { left: 43px; top: 223px; letter-spacing: 3px; color: #ffffff; }
</style>
</head>
<body>

  <span class="side-label side-label--one">Back 1</span>
  <span class="side-label side-label--two">Back 2</span>
  <span class="side-label side-label--three">Back 3</span>

  <section class="card card--front" aria-label="Card front">
    <div class="wordmark front-brand"><span class="wordmark__square"></span>NORVA</div>
    <div class="front-rule"></div>
    <p class="front-tagline">NORTHERN COUNCIL OF <span>VERIFIED ESTATE ADVISORS</span></p>
    <span class="contact-mark"></span>
    <ul class="contact-list">
      <li><b>T :</b>(555) 010 2847</li>
      <li><b>M :</b>(555) 010 6631</li>
      <li><b>E :</b>peter@norva.ca</li>
    </ul>
    <div class="holder">
      <p class="holder__name">Peter L. Harwood</p>
      <p class="holder__title">VERIFIED ESTATE ADVISOR</p>
    </div>
  </section>

  <section class="card card--back-light" aria-label="Card back, light">
    <div class="wordmark wordmark--centered faint-brand"><span class="wordmark__square"></span>NORVA</div>
    <p class="web web--centered">www.norva.ca</p>
  </section>

  <section class="card card--back-charcoal" aria-label="Card back, charcoal">
    <div class="wordmark wordmark--centered charcoal-brand"><span class="wordmark__square"></span>NORVA</div>
    <p class="web web--centered">www.norva.ca</p>
  </section>

  <section class="card card--back-slate" aria-label="Card back, slate">
    <div class="wordmark slate-brand"><span class="wordmark__square"></span>NORVA</div>
    <p class="web">www.norva.ca</p>
  </section>

</body>
</html>
```